Creative Brief
Brand Packaging Identity V
KALSO
Pose your way
Innovation and Creativity are the cornerstones in the foundation of KALSO. The most accurate quartz watches in the industry, ruggedized for use by those that live, work and play in truly adverse conditions. Water and Shock resistant, the line of technology used is advanced and inventive at the same time, for those whose usage demanded certain durability.
Jewelry
the back dial should consist of some art work as shown as an example in the briefing.

```html
<!DOCTYPE html>
<html lang="en">
<head>
<meta charset="utf-8">
<title>KALSO — Brand Packaging Identity</title>
<link rel="stylesheet" href="https://fonts.googleapis.com/css2?family=Cinzel:wght@500&family=Lato:wght@400;700&display=swap">
<style>
:root{
  --stage:#2b2a28;
  --panel-top:#4a463c;
  --panel-bottom:#1c1b18;
  --gold:#cbbd93;
  --ivory:#f1efea;
  --ink:#2a2823;
  --muted:#8c8678;
}
*{box-sizing:border-box;margin:0;padding:0}
html,body{width:1200px;height:961px;overflow:hidden;background:var(--stage)}
.canvas{position:relative;width:1200px;height:961px;font-family:"Lato",sans-serif}
.piece{position:absolute}
.panel{position:absolute;background:radial-gradient(ellipse at 50% 35%,var(--panel-top),var(--panel-bottom) 80%);border:1px solid rgba(0,0,0,.5)}
.panel.light{background:linear-gradient(180deg,#fbfaf7,#e4e1da)}
.brand{font-family:"Cinzel",serif;font-weight:500;color:var(--gold);letter-spacing:.12em;text-align:center;line-height:1;white-space:nowrap}
.brand.dark{color:var(--ink)}
.center{display:flex;align-items:center;justify-content:center;flex-direction:column}
.tiny{font-size:7px;color:var(--muted);letter-spacing:.05em;white-space:nowrap}
svg{position:absolute;overflow:visible}
.vertical{writing-mode:vertical-rl;transform:rotate(180deg)}
.photo{position:absolute;border-radius:6px}
</style>
</head>
<body>
<main class="canvas">

  <!-- Guarantee card, dark -->
  <section class="piece guarantee-card" style="left:47px;top:247px;width:156px;height:182px">
    <svg width="156" height="182" viewBox="0 0 156 182">
      <defs><radialGradient id="darkFill" cx="50%" cy="40%" r="70%"><stop offset="0" stop-color="#4a463c"/><stop offset="1" stop-color="#1c1b18"/></radialGradient></defs>
      <path d="M78 0 C110 30 156 70 156 104 A78 78 0 0 1 0 104 C0 70 46 30 78 0Z" fill="url(#darkFill)"/>
      <rect x="0" y="86" width="156" height="24" fill="#f1efea"/>
    </svg>
    <div class="brand" style="position:absolute;top:52px;width:156px;font-size:17px">KALSO</div>
    <div style="position:absolute;top:91px;left:14px;font-size:13px;color:var(--ink);font-weight:700">Guarantee Card</div>
    <div class="tiny" style="position:absolute;top:128px;width:156px;text-align:center">www.kalsotime.com</div>
  </section>

  <!-- Guarantee card, light -->
  <section class="piece guarantee-card-light" style="left:208px;top:252px;width:156px;height:177px">
    <svg width="156" height="177" viewBox="0 0 156 182" preserveAspectRatio="none">
      <path d="M78 0 C110 30 156 70 156 104 A78 78 0 0 1 0 104 C0 70 46 30 78 0Z" fill="#f1efea"/>
      <g stroke="#c9c5bb" stroke-width="1"><line x1="46" y1="92" x2="140" y2="92"/><line x1="46" y1="106" x2="140" y2="106"/><line x1="46" y1="120" x2="140" y2="120"/></g>
    </svg>
    <div class="brand dark" style="position:absolute;top:48px;width:156px;font-size:17px">KALSO</div>
    <div class="tiny" style="position:absolute;top:84px;left:16px;line-height:14px">Date<br>Model<br>Serial</div>
    <div class="tiny" style="position:absolute;top:140px;width:156px;text-align:center">Dealer stamp here</div>
  </section>

  <!-- Watch box dieline -->
  <section class="piece watch-box">
    <div class="panel center" style="left:416px;top:200px;width:151px;height:60px"><span class="brand" style="font-size:8px">Kalso</span></div>
    <div class="panel" style="left:377px;top:260px;width:39px;height:260px"><span class="brand vertical" style="position:absolute;left:14px;top:110px;font-size:8px">Kalso</span></div>
    <div class="panel center" style="left:416px;top:260px;width:151px;height:260px"><span class="brand" style="font-size:20px">KALSO</span><span class="tiny" style="margin-top:110px">www.kalsotime.com</span></div>
    <div class="panel" style="left:567px;top:260px;width:36px;height:260px"></div>
    <div class="piece" style="left:416px;top:528px;width:143px;height:36px;display:flex;gap:4px">
      <span style="flex:1;background:var(--ivory)"></span><span style="flex:1;background:var(--ivory)"></span><span style="flex:1;background:var(--ivory)"></span><span style="flex:1;background:var(--ivory)"></span><span style="flex:1;background:var(--ivory)"></span>
    </div>
  </section>

  <!-- Strap sleeves -->
  <section class="piece strap-sleeves">
    <div class="panel" style="left:645px;top:218px;width:52px;height:275px"></div>
    <div class="panel light" style="left:703px;top:218px;width:52px;height:275px"></div>
    <div class="panel center" style="left:761px;top:218px;width:52px;height:275px"><span class="brand" style="font-size:11px;margin-top:-80px">KALSO</span></div>
    <div class="panel light" style="left:819px;top:288px;width:44px;height:205px"></div>
  </section>

  <!-- Watch product photos -->
  <div class="photo" role="img" aria-label="Product photo: white-dial wristwatch with black leather strap" style="left:890px;top:205px;width:105px;height:178px;background:radial-gradient(circle at 50% 50%,#e6e6e3 0 28%,#3a3a38 60%,#2b2a28 80%)"></div>
  <div class="photo" role="img" aria-label="Product photo: black-dial wristwatch with black leather strap" style="left:1015px;top:205px;width:110px;height:178px;background:radial-gradient(circle at 50% 50%,#5a5850 0 28%,#2f2e2b 60%,#2b2a28 80%)"></div>

  <!-- Hang tags -->
  <section class="piece hang-tags">
    <svg style="left:870px;top:398px" width="84" height="112" viewBox="0 0 156 182" preserveAspectRatio="none">
      <path d="M78 0 C110 30 156 70 156 104 A78 78 0 0 1 0 104 C0 70 46 30 78 0Z" fill="#f1efea"/>
      <circle cx="78" cy="40" r="6" fill="#2b2a28"/>
    </svg>
    <div class="panel light center" style="left:962px;top:469px;width:84px;height:28px"><span class="brand dark" style="font-size:9px">KALSO</span></div>
    <svg style="left:1105px;top:392px" width="2" height="40"><line x1="1" y1="0" x2="1" y2="40" stroke="#a89c7a" stroke-width="1.5"/></svg>
    <div class="panel center" style="left:1068px;top:432px;width:78px;height:78px;border-radius:50%"><span class="brand" style="font-size:10px;margin-top:10px">KALSO</span></div>
  </section>

  <!-- Cross box dieline -->
  <section class="piece cube-box">
    <div class="panel" style="left:143px;top:494px;width:117px;height:109px"></div>
    <div class="panel" style="left:47px;top:603px;width:96px;height:112px"></div>
    <div class="panel center" style="left:143px;top:603px;width:117px;height:125px"><span class="brand" style="font-size:15px">KALSO</span></div>
    <div class="panel" style="left:260px;top:603px;width:98px;height:112px"></div>
    <div class="panel" style="left:143px;top:728px;width:117px;height:98px"></div>
  </section>

  <!-- Small box dieline -->
  <section class="piece small-box">
    <div class="panel" style="left:429px;top:603px;width:104px;height:34px"></div>
    <div class="panel" style="left:377px;top:648px;width:52px;height:122px"></div>
    <div class="panel center" style="left:429px;top:637px;width:104px;height:138px"><span class="brand" style="font-size:14px">KALSO</span></div>
    <div class="panel" style="left:533px;top:648px;width:44px;height:122px"></div>
    <div class="panel" style="left:429px;top:775px;width:104px;height:36px"></div>
  </section>

  <!-- Flat bag -->
  <section class="piece flat-bag">
    <div class="panel" style="left:603px;top:546px;width:182px;height:265px">
      <svg style="left:70px;top:22px" width="42" height="14"><rect x="1" y="1" width="40" height="12" rx="6" fill="none" stroke="#141310" stroke-width="2"/></svg>
      <div class="tiny" style="position:absolute;bottom:10px;width:100%;text-align:center">www.kalsotime.com</div>
    </div>
  </section>

  <!-- Shopping bag -->
  <section class="piece shopping-bag">
    <svg style="left:1000px;top:548px" width="104" height="46"><path d="M2 46 C10 0 94 0 102 46" fill="none" stroke="#a89c7a" stroke-width="2"/></svg>
    <div class="panel center" style="left:800px;top:592px;width:140px;height:219px"><span class="brand" style="font-size:14px">KALSO</span></div>
    <div class="panel center" style="left:940px;top:592px;width:224px;height:219px"><span class="brand" style="font-size:22px">KALSO</span><span class="tiny" style="position:absolute;bottom:10px">www.kalsotime.com</span></div>
  </section>

</main>
</body>
</html>
```